I need a label design/logo for a Shea Body Butter that I making. The body butter is made using Unrefined Shea Butter from Uganda. I have different mixes for the body butter depending on the Essential Oil used, for example - sweet orange, lavender, rosemary. The species of Shea tree in Uganda (Vitellaria Nilotica) is different from the one in West Africa (Vitellaria Paradoxa). As such, I would like the logo/label to have some reference to the Shea nut tree as well as the River Nile. Colours should be "fresh and earthy". I will be using round containers and I would like to be able to place the logo/label on round templates that I can stick on the containers. The name of the brand is "Tesi Ruka" Shea Body Butter.

```html
<!DOCTYPE html>
<html lang="en">
<head>
<meta charset="utf-8">
<title>Tesi Ruka – Shea Body Butter Label</title>
<link rel="stylesheet" href="https://fonts.googleapis.com/css2?family=Cinzel:wght@600;700&family=Montserrat:wght@700;800&display=swap">
<style>
  :root {
    --page-bg: #ffffff;
    --label-green: #8cc63f;
    --band-green: #066938;
    --brand-purple: #7b3f98;
    --tree-purple-light: #8c4fa8;
    --ink: #1a1a1a;
    --white: #ffffff;
  }
  html, body {
    margin: 0;
    padding: 0;
    width: 1200px;
    height: 1000px;
    overflow: hidden;
    background: var(--page-bg);
  }
  .canvas {
    display: block;
    width: 1200px;
    height: 1000px;
  }
  .label-disc { fill: var(--label-green); }
  .name-band { fill: var(--band-green); }
  .origin-arc-text {
    font-family: "Cinzel", serif;
    font-weight: 700;
    font-size: 23px;
    fill: var(--brand-purple);
    letter-spacing: 1px;
  }
  .origin-dot { fill: var(--brand-purple); }
  .brand-name {
    font-family: "Cinzel", serif;
    font-weight: 700;
    font-size: 46px;
    fill: var(--brand-purple);
  }
  .product-name {
    font-family: "Cinzel", serif;
    font-weight: 700;
    font-size: 29px;
    fill: var(--white);
    letter-spacing: 0.5px;
  }
  .ingredients-title {
    font-family: "Montserrat", sans-serif;
    font-weight: 800;
    font-size: 13px;
    fill: var(--ink);
    letter-spacing: 1px;
  }
  .ingredients-list {
    font-family: "Montserrat", sans-serif;
    font-weight: 700;
    font-size: 9.5px;
    fill: var(--ink);
  }
</style>
</head>
<body>
<svg class="canvas" viewBox="0 0 1200 1000" xmlns="http://www.w3.org/2000/svg">
  <defs>
    <clipPath id="label-shape">
      <circle cx="600" cy="500" r="256"/>
    </clipPath>
    <linearGradient id="tree-tone" x1="0" y1="0" x2="0" y2="1">
      <stop offset="0" stop-color="var(--tree-purple-light)"/>
      <stop offset="1" stop-color="var(--brand-purple)"/>
    </linearGradient>
    <path id="origin-arc" d="M 383 520 A 218 218 0 1 1 817 520"/>
  </defs>

  <g class="round-label">
    <circle class="label-disc" cx="600" cy="500" r="256"/>

    <text class="origin-arc-text">
      <textPath href="#origin-arc" startOffset="50%" text-anchor="middle" textLength="690" lengthAdjust="spacing">MADE FROM UNREFINED SHEA BUTTER FROM UGANDA</textPath>
    </text>
    <circle class="origin-dot" cx="386" cy="542" r="5.5"/>
    <circle class="origin-dot" cx="814" cy="542" r="5.5"/>

    <rect class="tree-emblem" x="468" y="336" width="264" height="212" rx="40"
          fill="url(#tree-tone)" role="img"
          aria-label="Purple silhouette of a shea nut tree standing on a curved ground line"/>

    <text class="brand-name" x="600" y="606" text-anchor="middle">Tesi Ruka</text>

    <rect class="name-band" x="330" y="626" width="540" height="51" clip-path="url(#label-shape)"/>
    <text class="product-name" x="600" y="662" text-anchor="middle">S<tspan font-size="23">HEA</tspan> B<tspan font-size="23">ODY</tspan> B<tspan font-size="23">UTTER</tspan></text>

    <text class="ingredients-title" x="600" y="702" text-anchor="middle">INGREDIENTS:</text>
    <text class="ingredients-list" x="600" y="718" text-anchor="middle">SHEA BUTTER, COCONUT OIL</text>
    <text class="ingredients-list" x="600" y="730" text-anchor="middle">&amp; ESSENTIAL OIL</text>
  </g>
</svg>
</body>
</html>
```